Agricultural Consulting Website

Provide a modern yet business like website for my new Agriculture Consulting Business in Australia called FenTrove. Whilst we are based in Australia we are targetting both domestic and international markets (especially in Asia). We are targetting corporate, small business, government and farmer clients. The design should compliment our logo also sourced through pixel guild. The webiste should be easy for me to keep updated on a regular basis without the need to go back to the designer.

Industry/Entity Type

Business

Requirements
Must have
• clean crisp feel
• be modern yet business like
• be able to be updated by myself easily

```html
<!DOCTYPE html>
<html lang="en">
<head>
<meta charset="utf-8">
<title>FenTrove Agriculture</title>
<link rel="stylesheet" href="https://fonts.googleapis.com/css2?family=Arimo:wght@400;700&family=Open+Sans:wght@400;600&display=swap">
<style>
:root{
  --page:#ffffff;
  --mint:#d4e6c8;
  --soil:#663300;
  --soil-dark:#4a2500;
  --leaf:#3c7a12;
  --leaf-dark:#1f5a08;
  --nav-bg:#eef4e8;
  --nav-text:#1e4d0a;
  --gold:#f4e75a;
  --white:#ffffff;
  --orange:#ff7a00;
  --yellow:#ffff00;
  --ink:#111111;
  --sans:"Arimo",Arial,sans-serif;
  --body:"Open Sans",Arial,sans-serif;
}
*{margin:0;padding:0;box-sizing:border-box}
html,body{width:1200px;height:900px;overflow:hidden;background:var(--page)}
.site{position:absolute;left:119px;top:0;width:965px;height:900px;background:var(--soil)}
.topbar{position:absolute;left:0;top:0;width:965px;height:85px;background:var(--mint);border-top:3px solid var(--soil-dark)}
.brand{position:absolute;left:143px;top:18px;display:flex;align-items:center;gap:10px;font-family:var(--sans);font-size:40px;color:var(--leaf)}
.brand-mark{width:50px;height:50px;background:var(--leaf)}
.social{position:absolute;left:687px;top:29px;display:flex;gap:12px}
.social span{width:25px;height:25px;border-radius:50%;background:#6b3a10;box-shadow:1px 2px 3px rgba(0,0,0,.45)}
.nav{position:absolute;left:143px;top:100px;width:678px;height:30px;background:var(--nav-bg);border-radius:6px;display:flex;align-items:center;justify-content:space-between;padding:0 24px 0 11px;font-family:var(--sans);font-size:11px;color:var(--nav-text);list-style:none}
.nav li.active{background:linear-gradient(var(--leaf),var(--leaf-dark));color:var(--white);padding:3px 12px;border-radius:2px}
.hero{position:absolute;left:143px;top:151px;width:678px;height:238px;background:linear-gradient(90deg,#5f9a1e 0%,#c8322a 30%,#7d5a2a 50%,#d46a1a 75%,#f0a040 100%);box-shadow:0 2px 6px rgba(0,0,0,.5)}
.updates{position:absolute;left:146px;top:416px;width:226px;height:384px;border:1px solid #fff3c0;border-radius:8px;background:linear-gradient(var(--orange) 0%,#ffc000 35%,var(--yellow) 55%,#ffd000 75%,var(--orange) 100%);box-shadow:0 1px 4px rgba(0,0,0,.5)}
.updates h2{font-family:var(--sans);font-weight:400;font-size:19px;text-align:center;color:var(--ink);margin:6px 12px 0;padding-bottom:3px;border-bottom:1px dotted var(--ink)}
.updates ul{list-style:none;margin:12px 3px 0 11px}
.updates li{position:relative;height:57px;padding:0 0 0 20px;font-family:var(--sans);font-size:11px;line-height:17px;letter-spacing:-0.1px;color:var(--ink);border-bottom:1px dotted var(--ink);margin:0 6px 0 6px;padding-left:14px;padding-top:2px}
.updates li:last-child{border-bottom:none}
.updates li::before{content:"»";position:absolute;left:-6px;top:1px;font-weight:700;font-size:14px}
.thumbs{position:absolute;left:14px;top:225px;display:grid;grid-template-columns:93px 93px;gap:9px 9px}
.photo{display:block;width:93px;height:68px;border:1px solid #ffffff}
.ph-field{background:linear-gradient(#9cc4e0 0%,#cfe0ea 35%,#4f8a2e 60%,#2c6a1a 100%)}
.ph-crop{background:linear-gradient(90deg,#6a8a3a,#b08060 45%,#5e7a30)}
.ph-grass{background:linear-gradient(#a8c890,#4e9a2e 40%,#3f8a20)}
.ph-house{background:linear-gradient(90deg,#d8d8c8,#f0ece0 40%,#c83020 75%,#e0dcd0)}
.welcome{position:absolute;left:397px;top:418px;width:424px}
.welcome h1,.services h2{font-family:var(--sans);font-weight:400;font-size:21px;color:var(--gold)}
.welcome p{margin-top:9px;font-family:var(--body);font-size:10.5px;line-height:17px;color:var(--white)}
.btn{position:absolute;left:718px;top:545px;width:79px;height:18px;border-radius:3px;background:linear-gradient(#f6a531,#d97a00);font-family:var(--body);font-size:9px;color:var(--white);text-align:center;line-height:18px}
.services{position:absolute;left:397px;top:569px;width:405px}
.services h2{padding-bottom:4px;border-bottom:1px solid #e8d8c0}
.cols{position:absolute;left:395px;top:619px;width:440px}
.col{position:absolute;top:0;width:140px}
.col h3{font-family:var(--sans);font-weight:400;font-size:14px;color:var(--gold)}
.col .photo{width:95px;height:70px;margin-top:12px;margin-left:1px}
.col p{margin-top:10px;font-family:var(--body);font-size:10px;line-height:17px;color:var(--white)}
.more{position:absolute;font-family:var(--sans);font-size:11px;color:var(--ink);top:170px}
.more::before{content:"» ";font-weight:700}
.footer{position:absolute;left:0;top:828px;width:965px;height:72px;background:var(--mint)}
.foot-brand{position:absolute;left:144px;top:7px;display:flex;align-items:center;gap:6px;font-family:var(--sans);font-size:20px;color:var(--leaf)}
.foot-brand span{width:28px;height:24px;background:var(--leaf)}
.copy{position:absolute;left:144px;top:39px;font-family:var(--body);font-size:11px;color:var(--ink)}
.foot-nav{position:absolute;right:143px;top:41px;font-family:var(--body);font-size:10px;color:var(--ink);word-spacing:3px}
</style>
</head>
<body>
<div class="site">
  <header class="topbar">
    <div class="brand"><span class="brand-mark"></span>FenTrove</div>
    <div class="social"><span></span><span></span><span></span><span></span></div>
  </header>
  <ul class="nav">
    <li class="active">Home</li><li>About</li><li>Product</li><li>Services</li><li>Clients</li><li>Media</li><li>Gallery</li><li>Resources</li><li>Careers</li><li>Contact us</li>
  </ul>
  <div class="hero" role="img" aria-label="Baskets of fresh vegetables and autumn produce"></div>

  <aside class="updates">
    <h2>UP DATES</h2>
    <ul>
      <li>Lorem ipsum dolor sit amet, consectetur adipiscing elit. Sed at ante.</li>
      <li>Lorem ipsum dolor sit amet, consectetur adipiscing elit. Sed at ante.</li>
      <li>Lorem ipsum dolor sit amet, consectetur adipiscing elit. Sed at ante.</li>
    </ul>
    <div class="thumbs">
      <span class="photo ph-field" role="img" aria-label="Irrigated crop field"></span>
      <span class="photo ph-crop" role="img" aria-label="Advisors inspecting maize crop"></span>
      <span class="photo ph-grass" role="img" aria-label="Farm workers in a green field"></span>
      <span class="photo ph-house" role="img" aria-label="Greenhouse worker holding a crate of tomatoes"></span>
    </div>
  </aside>

  <section class="welcome">
    <h1>Welcome to FenTrove Agriculture</h1>
    <p>Lorem ipsum dolor sit amet, consectetur adipiscing elit. Sed at ante. Mauris eleifend, quam a vulputate dictum, massa quam dapibus leo, eget vulputate orci purus ut lorem. In fringilla mi in ligula. Pellentesque aliquam quam vel dolor. t, tempus ac, aliquam molestie, varius ac, tellus. Vestibulum aliquam risus rutrum interdum.</p>
  </section>
  <div class="btn">Read more...</div>

  <section class="services"><h2>Our Services</h2></section>
  <div class="cols">
    <div class="col" style="left:0">
      <h3>Productivity</h3>
      <span class="photo ph-field" role="img" aria-label="Irrigated crop field"></span>
      <p>Lorem ipsum dolor sit amet, consectetur adipiscing elit. Sed at ante.</p>
    </div>
    <div class="col" style="left:142px">
      <h3>Consultation</h3>
      <span class="photo ph-crop" role="img" aria-label="Advisors inspecting maize crop"></span>
      <p>Lorem ipsum dolor sit amet, consectetur adipiscing elit. Sed at ante.</p>
    </div>
    <div class="col" style="left:288px">
      <h3>Employment</h3>
      <span class="photo ph-house" role="img" aria-label="Greenhouse worker holding a crate of tomatoes"></span>
      <p>Lorem ipsum dolor sit amet, consectetur adipiscing elit. Sed at ante.</p>
    </div>
    <span class="more" style="left:32px">Read more...</span>
    <span class="more" style="left:195px">Read more...</span>
    <span class="more" style="left:345px">Read more...</span>
  </div>

  <footer class="footer">
    <div class="foot-brand"><span></span>FenTrove</div>
    <p class="copy">@ 2013 FenTrove All Rights Reserved</p>
    <p class="foot-nav">Home &nbsp;| About | Product | Services | Clients | Gallery | Contact Us</p>
  </footer>
</div>
</body>
</html>
```